I am a Life Coaching and I have purchased the logo for my business. I need business cards

I need a business card design using the logo attached (but instead of the logo saying "Harbor" I need it to say "Open Horizon Coaching"

Target Market(s)

Middle-aged people

Industry/Entity Type

Life coaching

Contact Information for Business Card

Name, email address, phone number, website

Font styles to use
Serif
Sans Serif
Script

Colors
0094D4
00A9DD
6FCCEA
C7EBF8
E9F6FB
00AB8E
00BBA5
67D7C9
C6EFE9
E9F9F6
59FF00
82FF00
B8FF75
E3FFCB
F4FFEA

Requirements
Must have
• Logo and contact info above
Nice to have
• As close to the business card inspo attached as possible

```html
<!DOCTYPE html>
<html lang="en">
<head>
<meta charset="utf-8">
<title>Open Horizon Coaching – Business Card</title>
<link href="https://fonts.googleapis.com/css2?family=Roboto:wght@400;500&display=swap" rel="stylesheet">
<style>
  :root {
    --backdrop: #ecebe8;
    --card: #ffffff;
    --ink: #2b2b2b;
    --ink-soft: #4a4a4a;
    --sky: #8fd0e2;
    --sky-light: #c7ebf8;
    --sky-pale: #e9f6fb;
    --link: #8ab8e6;
  }
  * { box-sizing: border-box; margin: 0; padding: 0; }
  html, body {
    width: 1200px;
    height: 1200px;
    overflow: hidden;
    background: var(--backdrop);
    font-family: "Roboto", Arial, sans-serif;
  }
  .sheet {
    position: relative;
    width: 1200px;
    height: 1200px;
  }
  .card {
    position: absolute;
    top: 204px;
    width: 450px;
    height: 790px;
    background: var(--card);
    box-shadow: 0 8px 24px rgba(0,0,0,0.12);
  }
  .card--front { left: 104px; }
  .card--back { left: 643px; }

  /* Front */
  .brand {
    position: absolute;
    left: 0; right: 0;
    top: 230px;
    display: flex;
    flex-direction: column;
    align-items: center;
    gap: 26px;
  }
  .brand__disc {
    width: 120px;
    height: 120px;
    border-radius: 50%;
    border: 3px solid var(--sky);
  }
  .brand__name {
    font-weight: 500;
    font-size: 32px;
    color: var(--ink);
    letter-spacing: 0.5px;
  }
  .website {
    position: absolute;
    left: 0; right: 0;
    bottom: 32px;
    text-align: center;
    font-size: 19px;
    letter-spacing: 1.5px;
    color: var(--link);
  }

  /* Back */
  .decor {
    position: absolute;
    left: 0; right: 0; top: 0;
    height: 230px;
    background: radial-gradient(ellipse at 50% 10%, var(--sky-light) 0%, var(--sky-pale) 45%, rgba(255,255,255,0) 75%);
  }
  .holder {
    position: absolute;
    left: 0; right: 0;
    top: 354px;
    text-align: center;
  }
  .holder__name {
    font-size: 23px;
    color: var(--ink-soft);
  }
  .holder__role {
    font-size: 19px;
    color: var(--ink-soft);
    margin-top: 2px;
  }
  .contacts {
    position: absolute;
    left: 0; right: 0;
    top: 466px;
    list-style: none;
    display: flex;
    flex-direction: column;
    align-items: center;
    gap: 16px;
  }
  .contact {
    display: flex;
    flex-direction: column;
    align-items: center;
    gap: 2px;
  }
  .contact__icon {
    width: 20px;
    height: 20px;
    fill: none;
    stroke: var(--sky);
    stroke-width: 1.6;
  }
  .contact__text {
    font-size: 20px;
    color: var(--ink-soft);
  }
</style>
</head>
<body>
<main class="sheet">
  <section class="card card--front">
    <div class="brand">
      <div class="brand__disc"></div>
      <div class="brand__name">Open Horizon Coaching</div>
    </div>
    <div class="website">www.openhorizon.com</div>
  </section>

  <section class="card card--back">
    <div class="decor" role="img" aria-label="Soft blue brand decoration"></div>
    <div class="holder">
      <div class="holder__name">Daniel Reyes</div>
      <div class="holder__role">Coach</div>
    </div>
    <ul class="contacts">
      <li class="contact">
        <svg class="contact__icon" viewBox="0 0 20 20" aria-hidden="true">
          <circle cx="10" cy="10" r="8.5"/>
          <path d="M7 5.5l1.6 2.2-1 1.2c.6 1.3 1.6 2.3 2.9 2.9l1.2-1 2.2 1.6-.8 1.6c-3.6-.4-6.4-3.2-6.8-6.8z"/>
        </svg>
        <span class="contact__text">210 - 04512 07733</span>
      </li>
      <li class="contact">
        <svg class="contact__icon" viewBox="0 0 20 20" aria-hidden="true">
          <rect x="2" y="4.5" width="16" height="11" rx="1"/>
          <path d="M2.5 5l7.5 6 7.5-6"/>
        </svg>
        <span class="contact__text">d.reyes@mailbox</span>
      </li>
      <li class="contact">
        <svg class="contact__icon" viewBox="0 0 20 20" aria-hidden="true">
          <circle cx="10" cy="10" r="8"/>
        </svg>
        <span class="contact__text">daniel.reyes</span>
      </li>
      <li class="contact">
        <svg class="contact__icon" viewBox="0 0 20 20" aria-hidden="true">
          <circle cx="10" cy="10" r="8"/>
        </svg>
        <span class="contact__text">daniel.reyes</span>
      </li>
      <li class="contact">
        <svg class="contact__icon" viewBox="0 0 20 20" aria-hidden="true">
          <path d="M10 18s-5.5-6-5.5-9.5a5.5 5.5 0 0 1 11 0C15.5 12 10 18 10 18z" fill="var(--sky)" stroke="none"/>
          <circle cx="10" cy="8.5" r="2" fill="#fff" stroke="none"/>
        </svg>
        <span class="contact__text">38, Pine Avenue, Portland</span>
      </li>
    </ul>
  </section>
</main>
</body>
</html>
```